Letterhead/Envelope/Business Cards for law firm - Marlowe & Tesniere PLLC
Marlowe Tesniere
Letterhead/Envelope/Business Cards for law firm - Marlowe & Tesniere PLLC - Law
Creative Brief
Use same font as used in my logo
Open to any ideas
Simple
Doran P. Tesniere
Attorney
Marlowe & Tesniere PLLC 618 Briarmoss Court Plaza 375 North Galloway Avenue Louisville, Kentucky 40597
dtesniere@mtlegalgroup.example
www.mtlegalgroup.example
Licensed in Kentucky, Indiana & West Virginia
We are looking for design of letterhead, envelopes and business cards.
We want to use our logo. But we also need Marlowe & Tesniere, PLLC on the card/letterhead.

```html
<!DOCTYPE html>
<html lang="en">
<head>
<meta charset="utf-8">
<title>Marlowe &amp; Tesniere PLLC — Business Card</title>
<link rel="stylesheet" href="https://fonts.googleapis.com/css2?family=Cinzel:wght@400;600&display=swap">
<style>
  :root {
    --backdrop: #e9e6e1;
    --card: #ffffff;
    --ink: #1f1f1f;
    --muted: #4a4a4a;
    --accent: #d0202e;
    --strip-text: #ffffff;
  }
  * { margin: 0; padding: 0; box-sizing: border-box; }
  html, body {
    width: 1200px; height: 902px; overflow: hidden;
    background: var(--backdrop);
    font-family: "Cinzel", serif;
    color: var(--ink);
  }
  .business-card {
    position: absolute; left: 100px; top: 165px;
    width: 1000px; height: 572px;
    background: var(--card);
    box-shadow: 0 14px 36px rgba(0,0,0,0.22);
  }
  .side-strip {
    position: absolute; right: 0; top: 0;
    width: 72px; height: 100%;
    background: var(--accent);
  }
  .side-strip__web {
    position: absolute; left: 50%; top: 50%;
    transform: translate(-50%, -50%) rotate(90deg);
    white-space: nowrap;
    color: var(--strip-text);
    font-size: 17px; letter-spacing: 4px;
  }
  .firm-mark {
    position: absolute; left: 56px; top: 92px;
    display: flex; align-items: center; gap: 20px;
  }
  .firm-mark__square {
    width: 46px; height: 46px; background: var(--accent);
  }
  .firm-mark__name {
    font-size: 42px; font-weight: 400; letter-spacing: 3px;
    color: var(--ink); text-transform: uppercase;
  }
  .edge-pointer {
    position: absolute; left: 0; top: 316px;
  }
  .person {
    position: absolute; left: 62px; top: 318px;
  }
  .person__name {
    color: var(--accent); font-size: 27px; font-weight: 400; letter-spacing: 1px;
  }
  .person__title {
    color: var(--muted); font-size: 21px; margin-top: 4px; letter-spacing: 1px;
  }
  .contact-list {
    position: absolute; left: 560px; top: 262px;
    list-style: none;
    font-size: 15.5px; color: var(--muted); letter-spacing: 0.5px;
  }
  .contact-list li {
    display: flex; align-items: center; gap: 8px;
    height: 23px;
  }
  .contact-list .no-icon { padding-left: 24px; }
  .contact-icon { width: 16px; height: 16px; flex: none; }
</style>
</head>
<body>
  <div class="business-card">
    <div class="firm-mark">
      <div class="firm-mark__square"></div>
      <div class="firm-mark__name">Marlowe Tesniere</div>
    </div>

    <svg class="edge-pointer" width="16" height="26" viewBox="0 0 16 26">
      <polygon points="0,0 16,13 0,26" fill="var(--ink)"/>
    </svg>
    <div class="person">
      <div class="person__name">Doran P. Tesniere</div>
      <div class="person__title">Attorney</div>
    </div>

    <ul class="contact-list">
      <li>
        <svg class="contact-icon" viewBox="0 0 16 16"><circle cx="8" cy="8" r="8" fill="var(--accent)"/><path d="M8 3.5a2.6 2.6 0 0 0-2.6 2.6C5.4 8 8 12 8 12s2.6-4 2.6-5.9A2.6 2.6 0 0 0 8 3.5z" fill="#fff"/><circle cx="8" cy="6.1" r="0.9" fill="var(--accent)"/></svg>
        618 Briarmoss Court Plaza
      </li>
      <li class="no-icon">375 North Galloway Avenue</li>
      <li class="no-icon">Louisville, Kentucky 40597</li>
      <li>
        <svg class="contact-icon" viewBox="0 0 16 16"><circle cx="8" cy="8" r="8" fill="var(--accent)"/><path d="M5.2 4h1.6l.8 2-1 .8a5.5 5.5 0 0 0 2.6 2.6l.8-1 2 .8v1.6c0 .5-.4.9-.9.9A7 7 0 0 1 4.3 4.9c0-.5.4-.9.9-.9z" fill="#fff"/></svg>
        502-555-0148
      </li>
      <li>
        <svg class="contact-icon" viewBox="0 0 16 16"><circle cx="8" cy="8" r="8" fill="var(--accent)"/><rect x="5.5" y="3.5" width="5" height="9" rx="1" fill="#fff"/><rect x="6.4" y="4.6" width="3.2" height="5.6" fill="var(--accent)"/></svg>
        502-555-0172
      </li>
      <li>
        <svg class="contact-icon" viewBox="0 0 16 16"><circle cx="8" cy="8" r="8" fill="var(--accent)"/><rect x="4" y="6.5" width="8" height="5" rx="0.8" fill="#fff"/><rect x="5.5" y="3.5" width="5" height="3.5" fill="#fff"/></svg>
        502-555-0190
      </li>
      <li>
        <svg class="contact-icon" viewBox="0 0 16 16"><circle cx="8" cy="8" r="8" fill="var(--accent)"/><rect x="3.8" y="5" width="8.4" height="6" fill="#fff"/><path d="M3.8 5 8 8.4 12.2 5" stroke="var(--accent)" stroke-width="0.9" fill="none"/></svg>
        dtesniere@mtlegalgroup.example
      </li>
      <li>
        <svg class="contact-icon" viewBox="0 0 16 16"><circle cx="8" cy="8" r="8" fill="var(--accent)"/><circle cx="8" cy="8" r="4.3" stroke="#fff" stroke-width="1" fill="none"/><path d="M3.7 8h8.6M8 3.7c-2 2.4-2 6.2 0 8.6M8 3.7c2 2.4 2 6.2 0 8.6" stroke="#fff" stroke-width="0.8" fill="none"/></svg>
        www.mtlegalgroup.example
      </li>
    </ul>

    <div class="side-strip">
      <div class="side-strip__web">www.mtlegalgroup.example</div>
    </div>
  </div>
</body>
</html>
```